Easy Business Card / Presentation Cover Design Project

We are looking for a business card design, covers for powerpoint presentations for investors, and possibly simple stationary for a Chicago real estate development firm. Our new logo is attached below.

We rehab and provide newly constructed homes. We are not a real estate brokerage firm (i.e., agents such as Meridale 47) and only operate in the Chicago area.

In terms of design, sophisticated and high end that would appeal to investors (theme should resemble investment banks, hedge funds, private equity rather than tech startup).

Target Market(s)

Investors, banks, financing sources

Industry/Entity Type

Real Estate

Requirements
Must have
• Two deliverables here. 1) Business card 2) Covers for powerpoint presentation.

Must be able to look sophisticated and high end when printed. Please think through the type of printing that will be needed. Would prefer something that can be printed in raised ink but digital is ok as well.

Will be printed on heavy paper.

Business Card: Horizontal Layout, no black backgrounds,

For presentation front cover, should include logo only. For back cover, should include contact info. Horizontal and should not contain any information that will need to be changed (i.e. date or client name)
Nice to have
• Would like to have the edges colored but not required. Please show multiple designs
Should not have
• Should not have any die cut or embossed type of designs. Shape should be standard size.

We are not a design firm, a retail firm, or a consumer product firm.

Please do not incorporate a house, buildings, etc. This must be very professional looking.

```html
<!DOCTYPE html>
<html lang="en">
<head>
<meta charset="utf-8">
<title>Corvane Realty – Stationery and Presentation Cover</title>
<link rel="stylesheet" href="https://fonts.googleapis.com/css2?family=Lora:wght@400;700&family=Arimo:wght@700&display=swap">
<style>
  :root {
    --canvas-bg: #e3e4e5;
    --brand-blue: #4a9aee;
    --brand-blue-deep: #2f7fd8;
    --paper: #f7f8f9;
    --ink: #3b3f44;
    --ink-soft: #6f747a;
    --white: #ffffff;
    --serif: "Lora", Georgia, serif;
    --sans: "Arimo", Arial, sans-serif;
  }
  * { box-sizing: border-box; margin: 0; padding: 0; }
  html, body { width: 1200px; height: 1012px; overflow: hidden; }
  body { background: var(--canvas-bg); position: relative; font-family: var(--serif); color: var(--ink); }

  .section-label { position: absolute; left: 98px; font-family: var(--sans); font-size: 10px; font-weight: 700; color: #1d1f22; }
  .section-label--stationery { top: 50px; }
  .section-label--covers { top: 597px; }

  .piece { position: absolute; box-shadow: 0 2px 5px rgba(0,0,0,0.18); overflow: hidden; }

  /* soft area where the brand pattern sits */
  .brand-pattern { position: absolute; }

  /* envelope */
  .envelope { left: 224px; top: 68px; width: 362px; height: 182px; background: var(--brand-blue); }
  .envelope__window { position: absolute; left: 32px; top: 87px; width: 154px; height: 66px; background: #f4f5f6; border-radius: 3px; }
  .envelope .brand-pattern { right: -20px; bottom: -30px; width: 130px; height: 150px;
    background: radial-gradient(circle at 55% 50%, rgba(255,255,255,0.75) 0%, rgba(255,255,255,0.35) 45%, rgba(255,255,255,0) 70%); }

  /* business cards */
  .card { top: 271px; width: 149px; height: 84px; background: var(--paper); }
  .card--back { left: 268px; }
  .card--back .brand-pattern { inset: 0;
    background: radial-gradient(circle at 40% 50%, rgba(74,154,238,0.55) 0%, rgba(74,154,238,0.25) 40%, rgba(120,125,130,0.18) 60%, rgba(247,248,249,0) 78%); }
  .card--front { left: 439px; }
  .card__brand { position: absolute; left: 10px; top: 10px; display: flex; align-items: center; gap: 4px; }
  .card__brand-dot { width: 14px; height: 14px; border-radius: 50%; background: var(--brand-blue); }
  .card__brand-name { font-size: 8px; line-height: 1; color: var(--ink); }
  .card__person { position: absolute; left: 10px; top: 40px; font-size: 4.5px; color: var(--brand-blue); line-height: 1.3; }
  .card__person-name { font-weight: 700; letter-spacing: 0.2px; }
  .card__contact { position: absolute; left: 84px; top: 40px; font-size: 4px; color: var(--brand-blue); line-height: 1.6; }

  /* letterhead */
  .letterhead { left: 649px; top: 61px; width: 341px; height: 491px; background: var(--paper); }
  .letterhead__brand { position: absolute; left: 30px; top: 44px; display: flex; align-items: center; gap: 7px; }
  .letterhead__brand-dot { width: 30px; height: 30px; border-radius: 50%; background: var(--brand-blue); }
  .letterhead__brand-name { font-size: 17px; line-height: 1; color: var(--ink); }
  .letterhead__contact { position: absolute; left: 215px; top: 36px; font-size: 4.5px; line-height: 1.7; color: var(--brand-blue); }
  .letterhead__contact-title { font-size: 7px; letter-spacing: 0.6px; margin-bottom: 2px; }
  .letterhead__meta { position: absolute; left: 30px; top: 118px; font-size: 5.5px; font-weight: 700; line-height: 1.6; color: var(--ink); }
  .letterhead__body { position: absolute; left: 30px; top: 160px; width: 290px; font-size: 5.4px; line-height: 1.6; color: var(--ink-soft); }
  .letterhead__body p { margin-bottom: 7px; }
  .letterhead__signoff { margin-top: 12px; }
  .letterhead .brand-pattern { right: -10px; bottom: -10px; width: 170px; height: 150px;
    background: radial-gradient(circle at 55% 55%, rgba(74,154,238,0.6) 0%, rgba(74,154,238,0.3) 42%, rgba(110,115,120,0.15) 60%, rgba(247,248,249,0) 75%); }

  /* presentation covers */
  .cover { top: 618px; height: 344px; background: var(--brand-blue); color: var(--white); }
  .cover--front { left: 98px; width: 490px; }
  .cover--back { left: 602px; width: 491px; }
  .cover--front .brand-pattern { right: -60px; top: 10px; width: 250px; height: 330px;
    background: radial-gradient(circle at 60% 50%, rgba(255,255,255,0.6) 0%, rgba(255,255,255,0.3) 40%, rgba(255,255,255,0) 68%); }
  .cover--back .brand-pattern { right: -10px; top: -40px; width: 240px; height: 240px;
    background: radial-gradient(circle at 50% 45%, rgba(255,255,255,0.65) 0%, rgba(255,255,255,0.3) 42%, rgba(255,255,255,0) 70%); }
  .cover__brand { position: absolute; left: 48px; top: 118px; display: flex; align-items: center; gap: 20px; }
  .cover__brand-ring { width: 92px; height: 92px; border-radius: 50%; border: 3px solid var(--white); }
  .cover__brand-name { font-size: 50px; line-height: 0.95; font-weight: 400; color: var(--white); }
  .cover__brand-name span { display: block; font-size: 27px; letter-spacing: 2px; }
  .cover__contact { position: absolute; left: 0; right: 0; top: 262px; text-align: center; font-size: 16px; line-height: 1.22; }
</style>
</head>
<body>

  <div class="section-label section-label--stationery">Stationery Mock-Up</div>

  <div class="piece envelope">
    <div class="envelope__window"></div>
    <div class="brand-pattern" role="img" aria-label="Brand circle pattern in white"></div>
  </div>

  <div class="piece card card--back">
    <div class="brand-pattern" role="img" aria-label="Brand circle pattern in blue and grey"></div>
  </div>

  <div class="piece card card--front">
    <div class="card__brand">
      <div class="card__brand-dot"></div>
      <div class="card__brand-name">Corvane<br>Realty</div>
    </div>
    <div class="card__person">
      <div class="card__person-name">YOUR NAME HERE</div>
      <div>Position title here</div>
    </div>
    <div class="card__contact">
      <div>Str. Larkfield 14, USA</div>
      <div>Tel: +40 700 111 234</div>
      <div>Fax: +40 700 222 345</div>
      <div>www.corvanerealty.com</div>
    </div>
  </div>

  <div class="piece letterhead">
    <div class="letterhead__brand">
      <div class="letterhead__brand-dot"></div>
      <div class="letterhead__brand-name">Corvane<br>Realty</div>
    </div>
    <div class="letterhead__contact">
      <div class="letterhead__contact-title">CONTACT</div>
      <div>Str. Larkfield 14, USA</div>
      <div>Tel: +40 700 111 234</div>
      <div>Fax: +40 700 222 345</div>
      <div>www.corvanerealty.com</div>
    </div>
    <div class="letterhead__meta">
      <div>TO: Clara Pennick</div>
      <div>Subject: Order status</div>
      <div>Date: 30.01.2012</div>
    </div>
    <div class="letterhead__body">
      <p>Dear Ms. Clara Pennick,<br>We are pleased to confirm that your order has been received and is now being prepared by our team. Our staff will review every detail and contact you shortly with the next steps.</p>
      <p>The property documents are complete and will be delivered to your office this week for signature.</p>
      <p>Our financing partners have approved the proposed schedule, and construction will begin as planned once the final permits are issued by the city.</p>
      <p>Thank you for your continued trust. Please let us know if you have any questions about the project timeline or the terms of the agreement.</p>
      <p class="letterhead__signoff">Best regards,<br>Tomas Vell</p>
    </div>
    <div class="brand-pattern" role="img" aria-label="Brand circle pattern in blue and grey"></div>
  </div>

  <div class="section-label section-label--covers">Presentation Cover</div>

  <div class="piece cover cover--front">
    <div class="brand-pattern" role="img" aria-label="Brand circle pattern in white"></div>
    <div class="cover__brand">
      <div class="cover__brand-ring"></div>
      <div class="cover__brand-name">Corvane<span>Realty</span></div>
    </div>
  </div>

  <div class="piece cover cover--back">
    <div class="brand-pattern" role="img" aria-label="Brand circle pattern in white"></div>
    <div class="cover__contact">
      <div>Str. Larkfield 14, USA</div>
      <div>Tel: +40 700 111 234 Fax: +40 700 222 345</div>
      <div>www.corvanerealty.com</div>
    </div>
  </div>

</body>
</html>
```